Lacrosse Magazine Ad
Pell9kin
Lacrosse Magazine Ad -
Creative Brief
This magazine ad is about our non-for-profit organization Pell9kin. We want this Pell9kin ad to go along with our "Goal" Campaign. The first 2 ads from this campaign are attached. Pell9kin is an organization that spreads the game of lacrosse throughout Long Island, NY to underprivileged areas that don't have the sport of lacrosse. Pell9kin is a growing project and is always welcoming to those who are willing to help spread the game of lacrosse.
Anyone who is interested in lacrosse and cares about helping spread the game of lacrosse.
**Must say that Pell9kin is the non-for-profit side of Under the Bright Harbor Sky Lacrosse. -Pell9kin logo (attached) -Short and simple description of Pell9kin -Our website - www.pell9kin.example -Have a similar look to our 2 previous ads

```html
<!DOCTYPE html>
<html lang="en">
<head>
<meta charset="utf-8">
<title>Pell9kin – Spread the Game</title>
<link href="https://fonts.googleapis.com/css2?family=Arimo:wght@400;700&family=Anton&display=swap" rel="stylesheet">
<style>
  :root {
    --night: #000000;
    --night-glow: #3a1838;
    --grass-light: #5f9a2c;
    --grass-mid: #3f7a1c;
    --grass-dark: #22480c;
    --player-tone: #2b3350;
    --player-tone-light: #cfd3dc;
    --ink-white: #ffffff;
    --logo-ink: #1c5e8c;
    --footer-bg: #000000;
  }
  html, body {
    margin: 0;
    padding: 0;
    width: 1200px;
    height: 847px;
    overflow: hidden;
    background: var(--night);
  }
  .ad {
    position: relative;
    width: 1200px;
    height: 847px;
    overflow: hidden;
    font-family: "Arimo", Arial, sans-serif;
    color: var(--ink-white);
  }
  .night-sky {
    position: absolute;
    left: 0; top: 0;
    width: 1200px; height: 520px;
    background:
      radial-gradient(ellipse 520px 220px at 1000px -20px, var(--night-glow) 0%, rgba(58,24,56,0) 100%),
      var(--night);
  }
  .field {
    position: absolute;
    left: 0; top: 515px;
    width: 1200px; height: 277px;
    background: linear-gradient(180deg, var(--grass-dark) 0%, var(--grass-mid) 30%, var(--grass-light) 100%);
  }
  .player-photo {
    position: absolute;
    left: 120px; top: 150px;
    width: 300px; height: 370px;
    border-radius: 40% 40% 30% 30%;
    background: radial-gradient(ellipse at 50% 45%, var(--player-tone-light) 0%, var(--player-tone) 55%, rgba(0,0,0,0) 75%);
  }
  .quote {
    position: absolute;
    left: 600px; top: 160px;
    width: 560px;
    margin: 0;
    font-size: 16.5px;
    line-height: 20px;
    font-weight: 400;
  }
  .quote span { display: block; }
  .headline {
    position: absolute;
    left: 444px; top: 602px;
    margin: 0;
    font-family: "Anton", "Arimo", sans-serif;
    font-size: 42px;
    letter-spacing: 1px;
    font-weight: 400;
    text-shadow: 2px 3px 4px rgba(0,0,0,0.55);
  }
  .brand-tile {
    position: absolute;
    left: 1022px; top: 568px;
    width: 178px; height: 108px;
    background: var(--ink-white);
    display: flex;
    align-items: center;
    justify-content: center;
  }
  .brand-name {
    font-family: "Arimo", Arial, sans-serif;
    font-weight: 700;
    font-size: 34px;
    color: var(--logo-ink);
  }
  .footer {
    position: absolute;
    left: 0; top: 792px;
    width: 1200px; height: 55px;
    background: var(--footer-bg);
    display: flex;
    align-items: center;
    justify-content: space-between;
    padding: 0 14px;
    box-sizing: border-box;
    font-size: 12px;
  }
  .footer .url { font-weight: 700; }
</style>
</head>
<body>
<main class="ad">
  <div class="night-sky" role="img" aria-label="Dark night sky scattered with faint stars and a purple glow at the top right"></div>
  <div class="field" role="img" aria-label="Photograph of a lush green grass lacrosse field"></div>
  <div class="player-photo" role="img" aria-label="Photograph of a lacrosse player in a white and navy uniform leaping with his stick raised"></div>

  <p class="quote">
    <span>Impossible is just a big word thrown around by small men who</span>
    <span>find it easier to live in the world they’ve been given than to</span>
    <span>explore the power they have to change it.</span>
    <span>Impossible is not a fact. It’s an opinion.</span>
    <span>Impossible is not a declaration. It’s a dare.</span>
    <span>Impossible is temporary.</span>
    <span>Impossible is nothing.</span>
  </p>

  <h1 class="headline">SPREAD THE GAME !</h1>

  <div class="brand-tile"><span class="brand-name">Pell9kin</span></div>

  <footer class="footer">
    <span class="mission">Pell9kin is the non-for-profit side of Under the Bright Harbor Sky Lacrosse.&nbsp;&nbsp; Pell9kin is the non-for-profit side of Under the Bright Harbor Sky Lacrosse.</span>
    <span class="more-info">More information on <span class="url">www.pell9kin.example</span></span>
  </footer>
</main>
</body>
</html>
```